Wine Shop Banners

Banner graphic/images required
Require banner images to match the present online wine shop.

www.kelterhaus-traube.de

The wine-shop presently has a very clean, simple design, lots of white space, which is very much the trend at the moment.

Requirements
Images or graphic design for present banners visible on the homepage

The colour and feeling of the banners must fit in with the present clean, simple design.

Work required
3 large slide-card/banners (can be more) and 3 smaller fixed banners below. Please view website to see present position of banners.

LARGE BANNERS x 3

Something special with white background within the banner space
White background on each slide-card. Small individual graphic image in the middle of the slide card. This could be either a simple element of wine:
ingredients, fruit (grape), bottle, cork, old bottle label etc. just displaying one item on each slide-card. Preferably with high quality graphic features.

Note:
We are trying the steer away from the classic stereotype wineshop design. The image/s should have a higher, individual graphic touch, which gives the design something different. Sometimes such artistic work is displayed in steampunk or even in nostalgic design, which leaves the viewer slightly memorized with the content.
To clarify: we are not looking for a full steampunk design but possibly certain elements of this will give you an idea what we mean. That is to say, the design can go slightly in this direction without going over the top. Something small but very eye-catching.

SMALLER BANNERS x 3

One idea is:
Showing a symbol e.g. - discount sign "%" against a white background but again with a high graphic quality.

Target Market(s)

People interested in purchasing wine.
Ages approx. 25 to 65

Industry/Entity Type

Shop

Requirements
Must have
• Something special with white background
• Small individual graphic image in the middle of the slide card.
Nice to have
• The image/s should have a higher, individual graphic touch, which gives the design something different. Something that leaves the viewer slightly memorized with the content.
Should not have
• Not the typical classical design that is often seen on wine shops.

```html
<!DOCTYPE html>
<html lang="en">
<head>
<meta charset="utf-8">
<title>Book your wine tasting – banner</title>
<link rel="stylesheet" href="https://fonts.googleapis.com/css2?family=Ubuntu:wght@400;500;700&family=Lobster&display=swap">
<style>
  :root {
    --stage: #d9d9d9;
    --card: #ffffff;
    --wine: #b0244f;
    --tan: #a98a63;
    --leaf: #5f7e3a;
    --arrow: #9a9a9a;
    --arrow-muted: #cfcfcf;
  }
  * { margin: 0; padding: 0; box-sizing: border-box; }
  html, body {
    width: 1200px;
    height: 556px;
    overflow: hidden;
    background: var(--stage);
  }
  .banner {
    position: absolute;
    left: 94px;
    top: 81px;
    width: 1012px;
    height: 393px;
    background: var(--card);
    overflow: hidden;
  }
  .pour-visual {
    position: absolute;
    left: 0;
    top: 0;
    width: 93px;
    height: 100%;
    background: linear-gradient(180deg, #3a3a2e 0%, #8e1b22 22%, #f4eeee 38%, #b3222c 55%, #f2e8e8 66%, #9c1420 82%, #c8c8c8 100%);
  }
  .headline {
    position: absolute;
    left: 118px;
    top: 70px;
    font-family: "Ubuntu", sans-serif;
    font-weight: 700;
    font-size: 50px;
    line-height: 60px;
    letter-spacing: -1px;
    color: var(--wine);
    white-space: nowrap;
    z-index: 2;
  }
  .intro {
    position: absolute;
    left: 122px;
    top: 146px;
    font-family: "Ubuntu", sans-serif;
    font-weight: 400;
    font-size: 25px;
    line-height: 36px;
    color: var(--tan);
    white-space: pre;
  }
  .gift-line {
    position: absolute;
    left: 122px;
    top: 237px;
    font-family: "Lobster", cursive;
    font-size: 32px;
    line-height: 48px;
    color: var(--leaf);
  }
  .cork-visual {
    position: absolute;
    left: 535px;
    top: 145px;
    width: 452px;
    height: 212px;
    background: radial-gradient(ellipse at 68% 55%, #c9a97e 0%, #b38d63 35%, #8c7058 55%, #e9e4de 80%, #ffffff 100%);
  }
  .slider-nav {
    position: absolute;
    right: 12px;
    bottom: 14px;
    display: flex;
    gap: 10px;
  }
</style>
</head>
<body>
  <section class="banner">
    <div class="pour-visual" role="img" aria-label="Red wine pouring from a bottle into a glass"></div>

    <h1 class="headline">BOOK Y’R WINE TESTING</h1>
    <p class="intro">Lorem ipsum is simply dummy  text
of typesetting</p>
    <p class="gift-line">Surprise of wine Gifts for<br>Someone Special</p>

    <div class="cork-visual" role="img" aria-label="Corkscrew beside a stacked pyramid of vintage-dated wine corks"></div>

    <nav class="slider-nav" aria-label="Slide navigation">
      <svg width="12" height="20" viewBox="0 0 12 20" aria-label="Previous slide"><polyline points="10,2 2,10 10,18" fill="none" stroke="var(--arrow-muted)" stroke-width="2"/></svg>
      <svg width="12" height="20" viewBox="0 0 12 20" aria-label="Next slide"><polyline points="2,2 10,10 2,18" fill="none" stroke="var(--arrow)" stroke-width="2"/></svg>
    </nav>
  </section>
</body>
</html>
```